Business IT Services Billboard to attract local small businesses

We are Brivolane, a premier Managed Service Provider (MSP) specializing in comprehensive IT services and VOIP phone solutions exclusively for businesses. Our goal is to create a dynamic and visually engaging billboard advertisement that not only highlights our cutting-edge IT solutions but also emphasizes our state-of-the-art VOIP phone services. This billboard should communicate our commitment to providing innovative, reliable, and holistic technology solutions.
Target Market(s)
small business
Industry/Entity Type
Information Technology
Colors
Designer to choose colors to be used in the design.
Look and feel
Each slider illustrates characteristics of the customer's brand and the style your logo design should communicate.

```html
<!DOCTYPE html>
<html lang="en">
<head>
<meta charset="utf-8">
<title>Brivolane Billboard</title>
<link rel="stylesheet" href="https://fonts.googleapis.com/css2?family=Bebas+Neue&family=Poppins:wght@600;700&display=swap">
<style>
  :root {
    --backdrop: #c2c2c2;
    --board-white: #ffffff;
    --navy: #0b1a30;
    --brand-blue: #1877c2;
    --signal-orange: #e0510a;
    --ink: #1b1b1b;
  }
  html, body {
    margin: 0;
    padding: 0;
    width: 1038px;
    height: 1200px;
    overflow: hidden;
    background: var(--backdrop);
  }
  .canvas {
    position: relative;
    width: 1038px;
    height: 1200px;
  }
  .billboard {
    position: absolute;
    left: 39px;
    top: 461px;
    width: 960px;
    height: 278px;
    box-shadow: 0 4px 6px rgba(0, 0, 0, 0.35);
    background: var(--board-white);
  }
  .billboard svg { display: block; }
  .band-blue { fill: var(--brand-blue); }
  .band-navy { fill: var(--navy); }
  .band-url { fill: var(--signal-orange); }
  .brand-name {
    font-family: "Poppins", sans-serif;
    font-weight: 700;
    font-size: 50px;
    fill: var(--brand-blue);
  }
  .headline {
    font-family: "Bebas Neue", sans-serif;
    font-size: 108px;
    fill: var(--signal-orange);
  }
  .subheadline {
    font-family: "Poppins", sans-serif;
    font-weight: 700;
    font-size: 84px;
    fill: var(--board-white);
  }
  .tagline {
    font-family: "Poppins", sans-serif;
    font-weight: 600;
    font-size: 42px;
    fill: var(--ink);
  }
  .call-to-action {
    font-family: "Bebas Neue", sans-serif;
    font-size: 74px;
    fill: var(--ink);
  }
  .web-address {
    font-family: "Poppins", sans-serif;
    font-weight: 700;
    font-size: 54px;
    fill: var(--board-white);
  }
</style>
</head>
<body>
<main class="canvas">
  <section class="billboard">
    <svg viewBox="0 0 1559 452" width="960" height="278" xmlns="http://www.w3.org/2000/svg">
      <rect width="1559" height="452" fill="var(--board-white)"/>
      <polygon class="band-blue" points="0,0 1559,0 1559,238 353,238 283,10 0,10"/>
      <polygon class="band-navy" points="313,0 1559,0 1559,140 356,140"/>
      <polygon class="band-url" points="683,335 1559,335 1559,405 701,405"/>

      <text class="brand-name" x="48" y="172" textLength="228" lengthAdjust="spacingAndGlyphs">Brivolane</text>

      <text class="headline" x="380" y="113" textLength="1123" lengthAdjust="spacingAndGlyphs">SEAMLESS TECHNOLOGY SOLUTIONS</text>
      <text class="subheadline" x="385" y="221" textLength="1118" lengthAdjust="spacingAndGlyphs">FOR MODERN BUSINESSES</text>
      <text class="tagline" x="48" y="303" textLength="1449" lengthAdjust="spacingAndGlyphs">Innovative IT and VOIP Solutions Tailored for Your Business Success</text>
      <text class="call-to-action" x="48" y="397" textLength="613" lengthAdjust="spacingAndGlyphs">TRANSFORM YOUR TECH TODAY!</text>
      <text class="web-address" x="748" y="385" textLength="752" lengthAdjust="spacing">www.brivolane.com</text>
    </svg>
  </section>
</main>
</body>
</html>
```